revised: 'wexford joinery' logo -or- business card

we require a business card or a logo that can be used on a business card & other stationery

(i've just recently decided to open this contest up to logo designs as well - but if you have already been working on a card concept, please feel free to continue with it & submit!)

-

We design and build custom brackets and fixings for our customers and their castles, i.e. homes, offices, workshops, farms etc. Our products might be used to:
- brace or support structures, such as houses, decks, small bridges, etc.
- connect any building material to another
- or could simply be a unique piece that exists as a talking point

As part of our design process we would produce drawings/plans/blue prints/prototypes of the product. Our designs factor in multiple elements, from the materials being joined, the client's taste, and the overall durability demanded by the application - if necessary, the bracket may also be endorsed by a third party, such as a stuctural or mechanical engineer.

The build process takes part in our workshop and on the client's site - some elements may be manufactured off-site, depending on the design chosen and the materials used.

Our brackets are designed to our customers' tastes and could be made to be hidden within the structure or exposed to create interest. Our brackets can be large or small, or be neat with clean lines or take on more of an industrial look.
Updates

please note brief has been updated with a more specific description of our business activity

i have also added the final drawing that was used to water-jet the bracket shown in the photos

also, you will note i changed the title to 'logo + business card'

i don't expect a logo as a discrete artefact of the job, however, i expect that some or all elements on the face of the business card will lend themselves to the street sign (as stated in the original brief) as well as any future logo used on letter heads, invoices, etcetera

another update - changed the allowable entries to include logo's only, as well as business cards

Industry/Entity Type

Industrial

Requirements
Must have
• the face should have the name 'Wexford Joinery' (or no/all-caps)

the number '75' in the logo, which will also be turned into a conservative (residential) street sign ('75' being a street number) - '75' should stand alone -OR- be readily identified by someone who has previously received a business card

i need to make this '75' and any associated 'framing', so it should be transferrable to cad/dxf for machining, laser/water-cutting, brazing/welding, etcet.

(on that note, the winning designer will be able to share their vision for this sign and we'll adhere to it ... within the realms of possibility! if you're happy with the result then you could include it in your portfolio)
Nice to have
• one side of the card needs a majority of space for quotes, hand-written information, etcet. so this side should be white or a light, complimentary colour suitable for black/blue pen

the following should appear somewhere on the card (there is no email or website) :
- name : Mara Quell (Proprietor)
- mobile phone number : +61 (0) 498 716203
- abn: 58 604 917 235

any combination of the following (or equivalent) text:

* 'your castle' - this is slang for your house/place (i prefer this to 'home' as 1: it can apply to a place of business, and 2: for me at least, it conjurs images of wrought iron, brass, hardwood & stone)

* unique

* ...

```html
<!DOCTYPE html>
<html lang="en">
<head>
<meta charset="utf-8">
<title>Wexford Joinery – business card concepts</title>
<link href="https://fonts.googleapis.com/css2?family=Roboto:wght@300;400;500;700;900&family=Open+Sans:wght@700&display=swap" rel="stylesheet">
<style>
  :root {
    --bg: #ebeceb;
    --paper: #ffffff;
    --ink: #2a2a2a;
    --orange-warm: #ef8220;
    --orange: #e8661f;
    --rule: #c9c9c9;
    --edge: #d4d4d4;
    --label: #333333;
  }
  * { margin: 0; padding: 0; box-sizing: border-box; }
  html, body { width: 1200px; height: 1095px; overflow: hidden; background: var(--bg); }
  .sheet {
    position: relative; width: 1239px; height: 1131px;
    transform: scale(0.9686); transform-origin: 0 0;
    font-family: "Roboto", Arial, sans-serif;
  }
  .option-label { position: absolute; font-size: 28px; font-weight: 400; color: var(--label); }
  .card {
    position: absolute; width: 533px; height: 306px; overflow: hidden;
    background: var(--paper); border: 1px solid var(--edge);
  }
  .card > * { position: absolute; }
  .band-dark { background: var(--ink); left: 0; right: 0; }
  .band-orange { background: var(--orange); left: 0; right: 0; }
  .rule-orange { background: var(--orange); left: 0; right: 0; height: 6px; }
  .wordmark { font-weight: 900; text-transform: lowercase; letter-spacing: 1px; line-height: 1; white-space: nowrap; }
  .person { line-height: 1; white-space: nowrap; }
  .person .name { display: block; font-weight: 700; text-transform: uppercase; }
  .person .role { display: block; font-weight: 300; text-transform: uppercase; }
  .person .abn { display: block; }
  .phone { display: flex; align-items: center; gap: 6px; color: #fff; font-weight: 700; font-size: 29px; white-space: nowrap; }
  .phone svg { width: 26px; height: 28px; }
  .emblem { border-radius: 50%; }
  .write-lines { left: 0; right: 0; }
  .write-lines span { position: absolute; height: 1px; background: var(--rule); }
  .slogan { font-family: "Open Sans", Arial, sans-serif; font-weight: 700; color: #fff; font-size: 17px; letter-spacing: 1px; text-transform: uppercase; white-space: nowrap; }
</style>
</head>
<body>
<div class="sheet">

  <!-- Option 1 -->
  <div class="option-label" style="left:54px;top:98px;">1</div>
  <section class="card card-front" style="left:85px;top:60px;">
    <div class="wordmark" style="left:34px;top:24px;font-size:52px;color:var(--ink);line-height:54px;">wexford<br>joinery</div>
    <div class="rule-orange" style="top:133px;background:var(--orange-warm);"></div>
    <div class="band-dark" style="top:139px;height:102px;"></div>
    <div class="band-orange" style="top:241px;height:59px;background:var(--orange-warm);"></div>
    <div class="person" style="left:87px;top:150px;color:#fff;">
      <span class="name" style="font-size:24px;font-weight:500;">Mara Quell</span>
      <span class="role" style="font-size:21px;margin-top:6px;">Proprietor</span>
      <span class="abn" style="font-size:14px;font-weight:700;margin-top:10px;">ABN: 58 604 917 235</span>
    </div>
    <div class="phone" style="left:82px;top:250px;">
      <svg viewBox="0 0 24 24" aria-hidden="true"><path fill="#fff" d="M6.6 2.2c.6-.3 1.2 0 1.5.5l2 3.6c.3.6.2 1.2-.3 1.6L8.3 9c.9 2.6 3 5.2 5.5 6.6l1.3-1.4c.4-.5 1.1-.6 1.6-.3l3.5 2.1c.5.3.8 1 .5 1.5l-1 2.3c-.4.8-1.3 1.3-2.2 1.1C9.6 19.5 4 13.3 3.3 5.7c-.1-.9.4-1.8 1.2-2.2z"/></svg>
      <span>+61 (0) 498 716203</span>
    </div>
    <div class="emblem" style="left:345px;top:63px;width:144px;height:144px;background:var(--ink);"></div>
  </section>
  <section class="card card-back" style="left:663px;top:60px;height:303px;">
    <div class="write-lines" style="top:0;height:200px;">
      <span style="left:67px;width:391px;top:71px;"></span>
      <span style="left:67px;width:391px;top:109px;"></span>
      <span style="left:67px;width:391px;top:147px;"></span>
      <span style="left:67px;width:391px;top:185px;"></span>
    </div>
    <svg style="left:0;top:0;" width="533" height="303" viewBox="0 0 533 303" aria-hidden="true">
      <polygon points="0,262 533,210 533,252 0,302" fill="var(--orange-warm)"/>
      <polygon points="0,302 533,252 533,303 0,303" fill="var(--ink)"/>
    </svg>
    <div class="slogan" style="left:80px;top:234px;transform:rotate(-5.6deg);transform-origin:left center;font-size:18px;">Your slogan here&nbsp;&nbsp;your slogan here</div>
  </section>

  <!-- Option 2 -->
  <div class="option-label" style="left:50px;top:470px;">2</div>
  <section class="card card-front" style="left:86px;top:408px;height:307px;">
    <div class="band-dark" style="top:0;height:129px;"></div>
    <div class="wordmark" style="left:41px;top:16px;font-size:52px;color:#fff;line-height:54px;">wexford<br>joinery</div>
    <div class="rule-orange" style="top:129px;"></div>
    <div class="band-orange" style="top:248px;height:59px;"></div>
    <div class="person" style="left:92px;top:152px;color:var(--ink);">
      <span class="name" style="font-size:23px;">Mara Quell</span>
      <span class="role" style="font-size:21px;font-weight:400;margin-top:5px;">Proprietor</span>
      <span class="abn" style="font-size:16px;margin-top:15px;">ABN: 58 604 917 235</span>
    </div>
    <div class="phone" style="left:88px;top:257px;">
      <svg viewBox="0 0 24 24" aria-hidden="true"><path fill="#fff" d="M6.6 2.2c.6-.3 1.2 0 1.5.5l2 3.6c.3.6.2 1.2-.3 1.6L8.3 9c.9 2.6 3 5.2 5.5 6.6l1.3-1.4c.4-.5 1.1-.6 1.6-.3l3.5 2.1c.5.3.8 1 .5 1.5l-1 2.3c-.4.8-1.3 1.3-2.2 1.1C9.6 19.5 4 13.3 3.3 5.7c-.1-.9.4-1.8 1.2-2.2z"/></svg>
      <span>+61 (0) 498 716203</span>
    </div>
    <div class="emblem" style="left:345px;top:58px;width:156px;height:156px;background:var(--orange);"></div>
  </section>
  <section class="card card-back" style="left:665px;top:408px;height:306px;">
    <div class="write-lines" style="top:0;height:200px;">
      <span style="left:66px;width:392px;top:73px;"></span>
      <span style="left:66px;width:392px;top:111px;"></span>
      <span style="left:66px;width:392px;top:149px;"></span>
      <span style="left:66px;width:392px;top:187px;"></span>
    </div>
    <div class="band-orange" style="top:257px;height:49px;"></div>
    <div class="slogan" style="left:0;right:0;top:271px;text-align:center;">Your slogan here</div>
  </section>

  <!-- Option 3 -->
  <div class="option-label" style="left:45px;top:901px;">3</div>
  <section class="card card-front" style="left:86px;top:780px;height:307px;">
    <div class="band-dark" style="top:0;height:80px;"></div>
    <div class="wordmark" style="left:0;right:0;top:17px;text-align:center;font-size:46px;color:#fff;">wexford joinery</div>
    <div class="rule-orange" style="top:80px;"></div>
    <div class="band-orange" style="top:248px;height:59px;"></div>
    <div class="person" style="left:0;width:478px;top:128px;text-align:center;color:var(--ink);">
      <span class="name" style="font-size:23px;">Mara Quell</span>
      <span class="role" style="font-size:21px;font-weight:400;margin-top:8px;">Proprietor</span>
      <span class="abn" style="font-size:17px;margin-top:28px;">ABN: 58 604 917 235</span>
    </div>
    <div class="phone" style="left:91px;top:259px;">
      <svg viewBox="0 0 24 24" aria-hidden="true"><path fill="#fff" d="M6.6 2.2c.6-.3 1.2 0 1.5.5l2 3.6c.3.6.2 1.2-.3 1.6L8.3 9c.9 2.6 3 5.2 5.5 6.6l1.3-1.4c.4-.5 1.1-.6 1.6-.3l3.5 2.1c.5.3.8 1 .5 1.5l-1 2.3c-.4.8-1.3 1.3-2.2 1.1C9.6 19.5 4 13.3 3.3 5.7c-.1-.9.4-1.8 1.2-2.2z"/></svg>
      <span>+61 (0) 498 716203</span>
    </div>
    <div class="emblem" style="left:388px;top:108px;width:116px;height:116px;background:var(--ink);"></div>
  </section>
  <section class="card card-back" style="left:669px;top:778px;height:306px;">
    <div class="write-lines" style="top:0;height:200px;">
      <span style="left:73px;width:392px;top:72px;"></span>
      <span style="left:73px;width:392px;top:110px;"></span>
      <span style="left:73px;width:392px;top:147px;"></span>
      <span style="left:73px;width:392px;top:185px;"></span>
    </div>
    <div class="band-orange" style="top:247px;height:59px;"></div>
    <div class="slogan" style="left:0;right:0;top:267px;text-align:center;">Your slogan here</div>
  </section>

</div>
</body>
</html>
```